Surviving Domestic Violence Flyer

I need a flyer that "POPS" to attract participants for my research project. I have added the important information on my draft flyer.

```html
<!DOCTYPE html>
<html lang="en">
<head>
<meta charset="utf-8">
<title>Request For Study Participants</title>
<link rel="stylesheet" href="https://fonts.googleapis.com/css2?family=Oswald:wght@700&family=Roboto+Condensed:wght@700&family=Arimo:wght@400&display=swap">
<style>
  :root {
    --purple: #6a2467;
    --cyan: #3fb6d8;
    --yellow: #fff200;
    --white: #ffffff;
    --ink: #111111;
    --link: #ffe600;
    --photo-warm: #b07a4e;
    --photo-deep: #6e2a22;
  }
  * { box-sizing: border-box; margin: 0; padding: 0; }
  html, body { width: 900px; height: 1200px; overflow: hidden; background: var(--white); }
  .flyer {
    position: relative; width: 900px; height: 1200px; overflow: hidden;
    background: var(--purple);
  }
  .edge { position: absolute; left: 0; width: 900px; background: var(--cyan); }
  .edge--top { top: 0; height: 9px; }
  .edge--bottom { bottom: 0; height: 15px; }

  .header { position: absolute; top: 9px; left: 0; width: 900px; height: 213px; text-align: center; }
  .header__title {
    font-family: "Oswald", "Arial Narrow", sans-serif; font-weight: 700;
    color: var(--yellow); font-size: 60px; line-height: 1; letter-spacing: -0.5px;
    margin-top: 28px; transform: scaleX(0.8);
  }
  .header__subtitle {
    font-family: "Roboto Condensed", "Arial Narrow", sans-serif; font-weight: 700;
    color: var(--white); font-size: 39px; line-height: 46px; margin-top: 18px;
  }

  .body-panel { position: absolute; top: 222px; left: 0; width: 900px; height: 683px; background: var(--white); }
  .criteria {
    position: absolute; top: 302px; left: 8px; width: 515px; list-style: none; z-index: 2;
    font-family: "Roboto Condensed", "Arial Narrow", sans-serif; font-weight: 700;
    font-size: 25.5px; line-height: 59px; letter-spacing: -0.3px; color: var(--ink);
    white-space: nowrap;
  }
  .criteria li { padding-left: 16px; text-indent: -16px; }
  .criteria li::before { content: "• "; }

  .photo-frame {
    position: absolute; top: 215px; left: 510px; width: 392px; height: 693px;
    background: var(--white); border-radius: 8px 0 0 8px;
    box-shadow: -2px 2px 6px rgba(0,0,0,0.25);
  }
  .photo {
    position: absolute; top: 16px; left: 13px; width: 379px; height: 660px;
    background: linear-gradient(180deg, var(--photo-warm) 0%, var(--photo-deep) 100%);
  }

  .details {
    position: absolute; top: 937px; left: 14px; width: 876px;
    font-family: "Arimo", Arial, sans-serif; font-size: 17.5px; line-height: 22px; color: var(--white);
  }
  .details p { margin-bottom: 15px; }
  .details .note { margin-top: 26px; margin-bottom: 12px; }
  .details a { color: var(--link); text-decoration: underline; }
  .details .credits p { margin-bottom: 0; line-height: 24px; }
</style>
</head>
<body>
<div class="flyer">
  <div class="edge edge--top"></div>

  <header class="header">
    <h1 class="header__title">Request For Study Participants</h1>
    <h2 class="header__subtitle">EFFICIENCY OF RESOURCES AVAILABLE TO SUVIVORS<br>OF INTIMATE PARTNER ABUSE</h2>
  </header>

  <section class="body-panel"></section>

  <div class="photo-frame">
    <div class="photo" role="img" aria-label="Photograph illustrating the distress of domestic abuse"></div>
  </div>

  <ul class="criteria">
    <li>Are you eigteen years of age or older?</li>
    <li>Have you been a victim of domestic violence?</li>
    <li>Have you sough assistance with abuse<br>In the last 12 months?</li>
    <li>Are you still in contact with the person<br>Who abused you?</li>
    <li>Are you willing and open to discussing your<br>Experience with abuse and your attempts to<br>Access services or resources?</li>
  </ul>

  <section class="details">
    <p>If you answered yes to all of these questions, you may be eligible to participate in a study to better understand the resources needed and services expected for survivors of domestic violence.</p>
    <p>Please contact Dana Whitfield at 1(555)014-2280 of via e-mail <a href="mailto:survivorstudy@example.org">survivorstudy@example.org</a> for additional information.</p>
    <p class="note">Participants will be compensated for their time.</p>
    <div class="credits">
      <p>Principal Investigator: Dana Whitfield</p>
      <p>Institutional Affiliation: Lakeshore State University, Dept. of Criminology, Law, and Justice</p>
      <p>Contact Address: Post Office Box 120455, Chicago, IL, 60600</p>
    </div>
  </section>

  <div class="edge edge--bottom"></div>
</div>
</body>
</html>
```